Fontenot Bayou Grillhouse (Owners Card)

Need a classy, but modern business card. I have included a promotional card for the steakhouse. I need one for myself (the owner) that is more professional.

Target Market(s)

General Public

Industry/Entity Type

Food service

Contact Information for Business Card

Name, business address, phone number, email, logo

Font styles to use
Serif
Sans Serif
Decorative
Script

Requirements
Must have
• My name (Darvel Pruitt), business address (327 Oakmere Street), phone number (510) 493-2615, email (Dpruittkr4@mailvane.example. On the back of the card: Psalms 27 1 The LORD is my light and my salvation— whom shall I fear? The LORD is the stronghold of my life— of whom shall I be afraid? 2 When the wicked advance against me to devour me, it is my enemies and my foes who will stumble and fall. 3 Though an army besiege me, my heart will not fear; though war break out against me, even then I will be confident.
Nice to have
• Something that’s bold, but modern and professional.

```html
<!DOCTYPE html>
<html lang="en">
<head>
<meta charset="utf-8">
<title>Fontenot Bayou Grillhouse – Owner Card</title>
<link href="https://fonts.googleapis.com/css2?family=Cinzel:wght@700&family=Poppins:wght@400;600&display=swap" rel="stylesheet">
<style>
  :root {
    --backdrop: #777777;
    --card: #111111;
    --ink: #ffffff;
    --muted: #d9d9d9;
    --rule: #8a8a8a;
    --brand: #e9a23b;
  }
  * { box-sizing: border-box; margin: 0; padding: 0; }
  html, body { width: 1200px; height: 1000px; overflow: hidden; }
  body {
    background: var(--backdrop);
    position: relative;
    font-family: "Poppins", sans-serif;
    color: var(--ink);
  }
  .card {
    position: absolute;
    left: 293px;
    width: 613px;
    height: 351px;
    background: var(--card);
    border-radius: 30px;
    box-shadow: 0 18px 30px rgba(0,0,0,0.35);
  }
  .card--front { top: 133px; }
  .card--back { top: 517px; padding: 36px 38px 0 37px; }

  .brand {
    position: absolute;
    top: 212px;
    left: 0;
    width: 100%;
    text-align: center;
    font-family: "Cinzel", serif;
    font-weight: 700;
    color: var(--brand);
    font-size: 30px;
    line-height: 36px;
    letter-spacing: 0.5px;
  }
  .brand-mark {
    display: block;
    width: 14px; height: 14px;
    margin: 0 auto 14px;
    background: var(--brand);
    border-radius: 50%;
  }
  .brand { top: 60px; }

  .contact-row {
    position: absolute;
    top: 238px;
    left: 0;
    width: 100%;
    display: flex;
    justify-content: center;
    align-items: center;
  }
  .owner { text-align: right; padding-right: 15px; }
  .owner-name {
    font-family: "Cinzel", serif;
    font-weight: 700;
    font-size: 19px;
    line-height: 22px;
  }
  .owner-role {
    font-size: 12px;
    font-weight: 600;
    letter-spacing: 1.5px;
    line-height: 16px;
    text-transform: uppercase;
  }
  .divider { width: 1px; height: 34px; background: var(--rule); }
  .details { padding-left: 15px; font-size: 16px; line-height: 20px; }
  .details li { list-style: none; display: flex; align-items: center; gap: 8px; }
  .details svg { width: 13px; height: 13px; fill: var(--ink); flex: none; }

  .address {
    position: absolute;
    top: 314px;
    left: 0;
    width: 100%;
    text-align: center;
    font-size: 14px;
    color: var(--muted);
  }

  .verse-title {
    font-family: "Cinzel", serif;
    font-weight: 700;
    font-size: 24px;
    line-height: 30px;
    margin-bottom: 18px;
  }
  .verse {
    font-size: 17.5px;
    line-height: 22px;
    text-align: justify;
    margin-bottom: 22px;
  }
  .verse b { font-weight: 600; }
</style>
</head>
<body>
  <section class="card card--front">
    <div class="brand">
      <span class="brand-mark"></span>
      Fontenot Bayou<br>Grillhouse
    </div>
    <div class="contact-row">
      <div class="owner">
        <div class="owner-name">Darvel Pruitt</div>
        <div class="owner-role">Owner</div>
      </div>
      <div class="divider"></div>
      <ul class="details">
        <li>
          <svg viewBox="0 0 24 24"><path d="M6.6 10.8a15.1 15.1 0 0 0 6.6 6.6l2.2-2.2c.3-.3.7-.4 1-.2 1.1.4 2.3.6 3.6.6.6 0 1 .4 1 1V20c0 .6-.4 1-1 1A17 17 0 0 1 3 4c0-.6.4-1 1-1h3.5c.6 0 1 .4 1 1 0 1.3.2 2.5.6 3.6.1.3 0 .7-.2 1z"/></svg>
          (510) 493-2615
        </li>
        <li>
          <svg viewBox="0 0 24 24"><path d="M2 5h20v14H2z M2 5l10 8 10-8" fill="none" stroke="#fff" stroke-width="2.2"/></svg>
          Dpruittkr4@mailvane.example
        </li>
      </ul>
    </div>
    <p class="address">327 Oakmere St, Fairfield, CA 94533, EUA</p>
  </section>

  <section class="card card--back">
    <h2 class="verse-title">Psalms 27</h2>
    <p class="verse"><b>1</b> The LORD is my light and my salvation— whom shall I fear?</p>
    <p class="verse">The LORD is the stronghold of my life— of whom shall I be afraid?</p>
    <p class="verse"><b>2</b> When the wicked advance against me to devour me, it is my enemies and my foes who will stumble and fall.</p>
    <p class="verse"><b>3</b> Though an army besiege me, my heart will not fear; though war break out against me, even then I will be confident.</p>
  </section>
</body>
</html>
```